PeerLoop Background Image Needed

I need a PeerLoop background image for my personal PeerLoop profile page. The dimension is 1400 pixels wide X 350 pixels high.

I am a consultant for www.TallOrangeLeap.com. The logo files are located here:

https://www.filecratio.net/shr/fd/m8tq2wxe7ulpa3vzrcoyn/k?akey=pq4nwc7udtr2ghwkmxbe81ys3&vw=0

A single message in the background is:

"Give your business a Tall Orange Leap with a proven path to optimized sales"

```html
<!DOCTYPE html>
<html lang="en">
<head>
<meta charset="utf-8">
<title>Tall Orange Leap – PeerLoop profile background</title>
<link href="https://fonts.googleapis.com/css2?family=Inter:wght@400;500;600;700;800;900&display=swap" rel="stylesheet">
<style>
  :root{
    --board:#737373;
    --ink:#111111;
    --orange:#f26419;
    --arrow:#cfcfcf;
    --nav:#263b4b;
    --page:#f3f3f2;
    --card:#ffffff;
    --blue:#0a66c2;
    --slate:#2d3e50;
    --line:#d9d9d9;
  }
  *{box-sizing:border-box;margin:0;padding:0}
  html,body{width:1020px;height:1200px;overflow:hidden}
  body{position:relative;background:var(--board);font-family:"Inter",Arial,sans-serif;color:var(--ink)}

  /* ---------- banner ---------- */
  .banner{position:absolute;left:46px;width:928px;height:231px;overflow:hidden;
    background:
      radial-gradient(ellipse 120px 90px at 90px 150px,rgba(190,190,190,.55),transparent 70%),
      radial-gradient(ellipse 90px 120px at 260px 60px,rgba(205,205,205,.5),transparent 70%),
      radial-gradient(ellipse 140px 80px at 430px 190px,rgba(215,215,215,.45),transparent 70%),
      linear-gradient(90deg,#d6d6d6 0%,#e8e8e8 28%,#f4f4f4 52%,#fdfdfd 75%,#ffffff 100%);}
  .banner--plain{top:53px}
  .banner--boxed{top:331px}
  .banner--sentence{top:610px}
  .growth-arrows{position:absolute;inset:0;width:100%;height:100%}
  .growth-arrows polygon{fill:var(--arrow)}

  .brand{position:absolute;left:52px;top:46px;display:flex;align-items:center;gap:18px}
  .brand__dot{width:104px;height:104px;border-radius:50%;background:var(--orange)}
  .brand__name{font-weight:900;font-size:42px;line-height:44px;color:var(--ink);letter-spacing:.5px;text-transform:uppercase}

  .headline{position:absolute;left:485px;font-weight:800;font-size:35px;letter-spacing:-.2px;line-height:1;color:var(--ink)}
  .banner--plain .headline{top:72px}
  .headline--boxed{left:468px;top:52px;width:404px;height:64px;background:var(--orange);color:#fff;
    display:flex;align-items:center;justify-content:center}
  .tagline{position:absolute;left:485px;font-size:24px;line-height:31px;font-weight:500;color:var(--ink);width:430px}
  .banner--plain .tagline{top:110px}
  .banner--boxed .tagline{top:121px;left:483px}
  .statement{position:absolute;left:481px;top:62px;width:440px;font-size:28px;line-height:33px;font-weight:600;color:var(--ink)}

  /* ---------- profile page preview ---------- */
  .page{position:absolute;left:0;top:901px;width:1020px;height:299px;background:var(--page)}
  .topnav{position:absolute;left:0;top:0;width:1020px;height:33px;background:var(--nav);color:#fff}
  .topnav__mark{position:absolute;left:146px;top:6px;width:21px;height:21px;background:var(--blue);border-radius:2px}
  .topnav__search{position:absolute;left:175px;top:7px;width:180px;height:20px;background:#fff;border-radius:2px;
    font-size:9px;color:#333;display:flex;align-items:center;gap:4px;padding-left:7px}
  .topnav__item{position:absolute;top:4px;width:60px;margin-left:-30px;text-align:center;font-size:7.5px;line-height:9px}
  .topnav__item svg{display:block;margin:0 auto 2px;width:13px;height:13px}
  .topnav__divider{position:absolute;left:756px;top:0;width:1px;height:33px;background:rgba(255,255,255,.35)}

  .profile{position:absolute;left:146px;top:63px;width:510px;height:236px;background:var(--card);overflow:hidden}
  .profile__cover{position:absolute;left:0;top:0;width:510px;height:128px;overflow:hidden}
  .profile__cover .banner{left:0;top:0;transform:scale(.5495);transform-origin:0 0}
  .profile__edit{position:absolute;right:24px;top:20px;width:16px;height:16px;border-radius:50%;background:#fff}
  .profile__photo{position:absolute;left:17px;top:61px;width:102px;height:102px;border-radius:50%;border:4px solid #fff;
    background:radial-gradient(circle at 50% 40%,#e9c2a6 0%,#b98566 40%,#6b3a2e 75%,#4a2626 100%)}
  .btn{position:absolute;top:138px;height:21px;font-size:9.5px;font-weight:700;border-radius:2px;display:flex;align-items:center;justify-content:center}
  .btn--primary{left:296px;width:116px;background:var(--blue);color:#fff}
  .btn--ghost{left:418px;width:48px;border:1px solid #bbb;color:#555;font-weight:500}
  .pencil{position:absolute;left:478px;top:140px}
  .bar{position:absolute;height:10px;background:linear-gradient(90deg,#9d9d9d,rgba(200,200,200,0))}
  .chip{position:absolute;left:349px;width:14px;height:14px}

  .sidebar{position:absolute;left:671px;top:63px;width:201px}
  .sidebar__row{position:absolute;left:0;width:201px;height:14px}
  .sidebar__row .bar{left:0;top:2px;width:150px;height:7px}
  .sidebar__row i{position:absolute;left:176px;top:0;width:10px;height:10px;border:1px solid #777;border-radius:50%}
  .sidebar__rule{position:absolute;left:0;top:26px;width:201px;height:1px;background:var(--line)}
  .ads{position:absolute;left:0;top:62px;width:201px;height:169px;background:#fff;border:1px solid var(--line);
    display:flex;align-items:center;justify-content:center;text-align:center;font-weight:800;font-size:24px;line-height:30px;color:var(--slate)}
</style>
</head>
<body>

<!-- Version A: plain headline -->
<section class="banner banner--plain">
  <svg class="growth-arrows" viewBox="0 0 1604 400" preserveAspectRatio="none" aria-hidden="true">
    <polygon points="1285,410 1330,355 1375,410"/>
    <polygon points="1340,357 1385,302 1430,357 1407,357 1407,400 1363,400 1363,357"/>
    <polygon points="1407,305 1452,250 1497,305 1474,305 1474,400 1430,400 1430,305"/>
    <polygon points="1475,254 1520,199 1565,254 1542,254 1542,400 1498,400 1498,254"/>
    <polygon points="1541,204 1586,149 1631,204 1608,204 1608,400 1568,400 1568,204"/>
  </svg>
  <div class="brand"><span class="brand__dot"></span><span class="brand__name">Tall<br>Orange<br>Leap</span></div>
  <h2 class="headline">GIVE YOUR BUSINESS</h2>
  <p class="tagline">a Tall Orange Leap with a proven path to optimized sales</p>
</section>

<!-- Version B: headline in orange box -->
<section class="banner banner--boxed">
  <svg class="growth-arrows" viewBox="0 0 1604 400" preserveAspectRatio="none" aria-hidden="true">
    <polygon points="1285,410 1330,355 1375,410"/>
    <polygon points="1340,357 1385,302 1430,357 1407,357 1407,400 1363,400 1363,357"/>
    <polygon points="1407,305 1452,250 1497,305 1474,305 1474,400 1430,400 1430,305"/>
    <polygon points="1475,254 1520,199 1565,254 1542,254 1542,400 1498,400 1498,254"/>
    <polygon points="1541,204 1586,149 1631,204 1608,204 1608,400 1568,400 1568,204"/>
  </svg>
  <div class="brand"><span class="brand__dot"></span><span class="brand__name">Tall<br>Orange<br>Leap</span></div>
  <h2 class="headline headline--boxed">GIVE YOUR BUSINESS</h2>
  <p class="tagline">a Tall Orange Leap with a proven path to optimized sales</p>
</section>

<!-- Version C: single sentence -->
<section class="banner banner--sentence">
  <svg class="growth-arrows" viewBox="0 0 1604 400" preserveAspectRatio="none" aria-hidden="true">
    <polygon points="1285,410 1330,355 1375,410"/>
    <polygon points="1340,357 1385,302 1430,357 1407,357 1407,400 1363,400 1363,357"/>
    <polygon points="1407,305 1452,250 1497,305 1474,305 1474,400 1430,400 1430,305"/>
    <polygon points="1475,254 1520,199 1565,254 1542,254 1542,400 1498,400 1498,254"/>
    <polygon points="1541,204 1586,149 1631,204 1608,204 1608,400 1568,400 1568,204"/>
  </svg>
  <div class="brand"><span class="brand__dot"></span><span class="brand__name">Tall<br>Orange<br>Leap</span></div>
  <p class="statement">Give your business a Tall Orange Leap with a proven path to optimized sales</p>
</section>

<!-- Profile page preview -->
<section class="page">
  <header class="topnav">
    <span class="topnav__mark"></span>
    <div class="topnav__search">
      <svg width="8" height="8" viewBox="0 0 10 10" aria-hidden="true"><circle cx="4" cy="4" r="3" fill="none" stroke="#333" stroke-width="1.5"/><line x1="6.3" y1="6.3" x2="9.3" y2="9.3" stroke="#333" stroke-width="1.5"/></svg>
      Search
    </div>
    <div class="topnav__item" style="left:473px"><svg viewBox="0 0 14 14" aria-hidden="true"><path d="M2 7 7 2 12 7V12H2Z" fill="none" stroke="#fff"/><circle cx="11" cy="3" r="2.5" fill="#e0282e"/></svg>Home</div>
    <div class="topnav__item" style="left:524px"><svg viewBox="0 0 14 14" aria-hidden="true"><circle cx="5" cy="5" r="2.5" fill="none" stroke="#fff"/><circle cx="10" cy="5" r="2" fill="none" stroke="#fff"/><path d="M1 13C1 9 9 9 9 13M9 9.5C12 9 13 11 13 13" fill="none" stroke="#fff"/></svg>My Network</div>
    <div class="topnav__item" style="left:575px"><svg viewBox="0 0 14 14" aria-hidden="true"><rect x="1.5" y="4" width="11" height="8" fill="none" stroke="#fff"/><path d="M5 4V2H9V4M1.5 7.5H12.5" fill="none" stroke="#fff"/></svg>Jobs</div>
    <div class="topnav__item" style="left:627px"><svg viewBox="0 0 14 14" aria-hidden="true"><rect x="1.5" y="3" width="11" height="8" fill="none" stroke="#fff"/><path d="M1.5 3 7 8 12.5 3" fill="none" stroke="#fff"/></svg>Messaging</div>
    <div class="topnav__item" style="left:678px"><svg viewBox="0 0 14 14" aria-hidden="true"><path d="M3 10V6A4 4 0 0 1 11 6V10L12 11H2Z M6 12H8" fill="none" stroke="#fff"/></svg>Notifications</div>
    <div class="topnav__item" style="left:730px"><svg viewBox="0 0 14 14" aria-hidden="true"><circle cx="7" cy="7" r="6.5" fill="#fff"/></svg>Me ▾</div>
    <span class="topnav__divider"></span>
    <div class="topnav__item" style="left:780px"><svg viewBox="0 0 14 14" aria-hidden="true"><g fill="#fff"><rect x="1" y="1" width="3" height="3"/><rect x="5.5" y="1" width="3" height="3"/><rect x="10" y="1" width="3" height="3"/><rect x="1" y="5.5" width="3" height="3"/><rect x="5.5" y="5.5" width="3" height="3"/><rect x="10" y="5.5" width="3" height="3"/><rect x="1" y="10" width="3" height="3"/><rect x="5.5" y="10" width="3" height="3"/><rect x="10" y="10" width="3" height="3"/></g></svg>Work ▾</div>
    <div class="topnav__item" style="left:839px;top:9px;width:70px;margin-left:-35px">Reactivate<br>Premium</div>
  </header>

  <article class="profile">
    <div class="profile__cover">
      <section class="banner banner--boxed">
        <svg class="growth-arrows" viewBox="0 0 1604 400" preserveAspectRatio="none" aria-hidden="true">
          <polygon points="1285,410 1330,355 1375,410"/>
          <polygon points="1340,357 1385,302 1430,357 1407,357 1407,400 1363,400 1363,357"/>
          <polygon points="1407,305 1452,250 1497,305 1474,305 1474,400 1430,400 1430,305"/>
          <polygon points="1475,254 1520,199 1565,254 1542,254 1542,400 1498,400 1498,254"/>
          <polygon points="1541,204 1586,149 1631,204 1608,204 1608,400 1568,400 1568,204"/>
        </svg>
        <div class="brand"><span class="brand__dot"></span><span class="brand__name">Tall<br>Orange<br>Leap</span></div>
        <h2 class="headline headline--boxed">GIVE YOUR BUSINESS</h2>
        <p class="tagline">a Tall Orange Leap with a proven path to optimized sales</p>
      </section>
      <span class="profile__edit"><svg width="16" height="16" viewBox="0 0 16 16" aria-hidden="true"><path d="M5 11 6 8 10.5 3.5 12.5 5.5 8 10Z" fill="none" stroke="#333"/></svg></span>
    </div>
    <div class="profile__photo" role="img" aria-label="Profile portrait photo of the consultant"></div>
    <span class="btn btn--primary">Add profile section ▾</span>
    <span class="btn btn--ghost">More...</span>
    <svg class="pencil" width="16" height="16" viewBox="0 0 16 16" aria-hidden="true"><path d="M3 13 4 9.5 11 2.5 13.5 5 6.5 12Z M9.5 4 12 6.5" fill="none" stroke="#0a66c2" stroke-width="1.4"/></svg>
    <span class="bar" style="left:16px;top:175px;width:125px"></span>
    <span class="bar" style="left:16px;top:193px;width:215px"></span>
    <span class="bar" style="left:16px;top:211px;width:215px"></span>
    <span class="chip" style="top:173px;background:#f47c62"></span>
    <span class="chip" style="top:193px;background:#b4bcc4"></span>
    <span class="bar" style="left:370px;top:175px;width:125px"></span>
    <span class="bar" style="left:370px;top:195px;width:125px"></span>
  </article>

  <aside class="sidebar">
    <div class="sidebar__row" style="top:3px"><span class="bar"></span><i></i></div>
    <span class="sidebar__rule"></span>
    <div class="sidebar__row" style="top:40px"><span class="bar"></span><i></i></div>
    <div class="ads">BUSINESS<br>ADS</div>
  </aside>
</section>

</body>
</html>
```